50c wing mondays

We need a sign reading the following.

HEADING: (large font as the focus of the sign)

50c wing Mondays
from 6pm till late

Medium font under the picture

YOUR CHOICE
- spiced buffalo wings
- hickory smoked BBQ
- Peri Peri

Small font
conditions apply
- minimum 4 wings per serving (of the same type)
- dine in only
- no discount apply

age 18 - 35

50c wing Mondays

Character Logo
• chalkduster

000000
f37122
ffffff

• Our logo
• A picture of wings
• FONT: chalkduster
• Background: BLACK
• Font colour: ORANGE
• Logo: Attached cinder kettle logo
• every word ive stated in the project description
• HEADING MUST BE LARGE: 50c Extra large - - - WING MONDAYS: LARGE
• The rest of the working small
• clip art - too many colours

```html
<!DOCTYPE html>
<html lang="en">
<head>
<meta charset="utf-8">
<title>50c Wing Mondays</title>
<link rel="stylesheet" href="https://fonts.googleapis.com/css2?family=Chicle&family=Tinos&display=swap">
<style>
  :root {
    --bg: #000000;
    --orange: #f7941d;
    --white: #ffffff;
    --art-deep: #b81e1e;
    --art-warm: #f37122;
    --art-light: #f9c23c;
  }
  html, body {
    margin: 0;
    padding: 0;
    width: 1200px;
    height: 1200px;
    overflow: hidden;
    background: var(--bg);
  }
  .sign {
    position: relative;
    width: 1200px;
    height: 1200px;
    background: var(--bg);
  }
  .line {
    position: absolute;
    left: 0;
    width: 1152px;
    margin: 0;
    text-align: center;
    line-height: 1;
    white-space: nowrap;
  }
  .price {
    top: 346px;
    font-family: "Chicle", cursive;
    font-size: 112px;
    color: var(--orange);
  }
  .title {
    top: 486px;
    font-family: "Chicle", cursive;
    font-size: 70px;
    letter-spacing: 2px;
    color: var(--orange);
  }
  .wing-art {
    position: absolute;
    left: 360px;
    top: 588px;
    width: 426px;
    height: 168px;
  }
  .flavours {
    top: 782px;
    font-family: "Tinos", serif;
    font-size: 53px;
    color: var(--orange);
  }
  .condition {
    font-family: "Tinos", serif;
    font-size: 43px;
    color: var(--white);
  }
  .condition--serving { top: 874px; }
  .condition--dine { top: 926px; }
  .condition--discount {
    top: 976px;
    letter-spacing: 0.5em;
    padding-left: 0.5em;
  }
</style>
</head>
<body>
  <main class="sign">
    <h1 class="line price">50c</h1>
    <h2 class="line title">WING MONDAYS</h2>

    <svg class="wing-art" role="img" aria-label="Illustration of a wooden barrel tipped on its side with a spill of food in warm red, orange and yellow" viewBox="0 0 426 168">
      <defs>
        <radialGradient id="artTone" cx="45%" cy="50%" r="60%">
          <stop offset="0%" stop-color="var(--art-light)"/>
          <stop offset="50%" stop-color="var(--art-warm)"/>
          <stop offset="100%" stop-color="var(--art-deep)"/>
        </radialGradient>
      </defs>
      <ellipse cx="213" cy="84" rx="213" ry="84" fill="url(#artTone)" opacity="0.85"/>
    </svg>

    <p class="line flavours">hickory - peri peri - spicy</p>
    <p class="line condition condition--serving">minimum 4 wings per serving</p>
    <p class="line condition condition--dine">- dine in only -</p>
    <p class="line condition condition--discount">no discounts apply</p>
  </main>
</body>
</html>
```